Ardenwell Building and Property Services needs a business card design

We need a business card design for our building and property services business. We already have a logo we just need a creative design and layout on a business card. Emphasis on clean, modern, professional.
Our client targets are mainly body corporates, building managers, construction managers.
We are a building services company that lean more to structural repair of buildings, through concrete rectification and carbon fibre strengthening.
We also refurbish facades, rendering, painting etc
We target higher end body corporates in prestigious locations, hence why we'd like our cards to reflect professionalism, strength, efficiency

Target Market(s)

body corporates, building managers, construction managers

Industry/Entity Type

Construction

Contact Information for Business Card

Ardenwell is the main word, with 'Building and Property Services' underneath.
Level 17, 82 Harlow Street
MERRIDALE
Melbourne
Vic 3094
T: 9518 2736
Duncan Ferris - Director
dunardenwell@mailbox-example.com

Requirements
Must have
• Stand out on the back of the card- strong/ bold, company logo
• All of the contact details written above
Should not have
• I'd like the card to stand out, especially on the back. Id like the company logo to be prominent, although feel free to be creative around it. But remain clean and professional

```html
<!DOCTYPE html>
<html lang="en">
<head>
<meta charset="utf-8">
<title>Ardenwell Business Card</title>
<link href="https://fonts.googleapis.com/css2?family=Open+Sans:wght@400;600;700&display=swap" rel="stylesheet">
<style>
  :root {
    --stage: #2b2b2b;
    --white: #ffffff;
    --blue-deep: #0b4f9c;
    --blue-mid: #1479c9;
    --blue-bright: #1fb0e8;
    --blue-brand: #1a8fd6;
    --edge-grey: #b9bec4;
    --map-tone: rgba(10, 70, 150, 0.28);
  }
  * { margin: 0; padding: 0; box-sizing: border-box; }
  html, body {
    width: 1200px; height: 907px; overflow: hidden;
    background: var(--stage);
    font-family: "Open Sans", Arial, sans-serif;
  }
  .canvas { position: relative; width: 1200px; height: 907px; }
  .card {
    position: absolute; width: 520px; height: 300px;
    border-radius: 3px; overflow: hidden;
    box-shadow: 0 14px 30px rgba(0,0,0,0.55);
  }
  .card-front { left: 50px; top: 150px; background: linear-gradient(135deg, var(--blue-deep) 30%, var(--blue-mid) 65%, var(--blue-bright)); }
  .card-back { left: 630px; top: 457px; background: linear-gradient(200deg, var(--blue-deep) 0%, var(--blue-mid) 45%, var(--blue-bright) 100%); }
  .front-shape { position: absolute; inset: 0; }
  .brand {
    position: absolute; display: flex; flex-direction: column; align-items: center;
    color: var(--blue-brand); font-weight: 600; text-align: center;
  }
  .brand-mark {
    width: 34px; height: 34px; border-radius: 50%;
    background: var(--blue-brand); margin-bottom: 12px;
  }
  .brand-name { font-size: 26px; letter-spacing: 4px; text-transform: uppercase; line-height: 1; }
  .brand-tagline { font-size: 7.5px; letter-spacing: 1.6px; text-transform: uppercase; margin-top: 5px; }
  .front-brand { left: 22px; top: 98px; width: 220px; }
  .contact {
    position: absolute; left: 300px; top: 40px; color: var(--white);
    font-size: 12px; line-height: 1.45;
  }
  .contact-name { font-size: 16px; font-weight: 700; text-transform: uppercase; letter-spacing: 0.3px; }
  .contact-role { font-size: 12px; margin-bottom: 18px; }
  .contact-address { margin-bottom: 14px; }
  .contact-line { display: flex; align-items: center; gap: 7px; font-size: 11.5px; }
  .contact-icon { width: 13px; height: 13px; flex: none; }
  .map-area {
    position: absolute; left: 70px; top: 40px; width: 400px; height: 230px;
    background: radial-gradient(ellipse at center, var(--map-tone), rgba(10,70,150,0) 70%);
  }
  .back-brand { left: 0; right: 0; top: 100px; color: var(--white); }
  .back-brand .brand-mark { background: var(--white); width: 40px; height: 40px; }
  .back-brand .brand-name { font-size: 30px; }
</style>
</head>
<body>
<div class="canvas">

  <section class="card card-front" aria-label="Card front">
    <svg class="front-shape" viewBox="0 0 520 300" width="520" height="300" aria-hidden="true">
      <polygon points="0,0 215,0 268,150 215,300 0,300" fill="var(--edge-grey)" transform="translate(5,0)"/>
      <polygon points="0,0 215,0 268,150 215,300 0,300" fill="var(--white)"/>
    </svg>
    <div class="brand front-brand">
      <span class="brand-mark"></span>
      <span class="brand-name">Ardenwell</span>
      <span class="brand-tagline">Building and Property Services</span>
    </div>
    <div class="contact">
      <p class="contact-name">Duncan Ferris</p>
      <p class="contact-role">Director</p>
      <p class="contact-address">Level 17, 82 Harlow Street<br>MERRIDALE, Melbourne<br>Vic 3094</p>
      <p class="contact-line">
        <svg class="contact-icon" viewBox="0 0 14 14" aria-hidden="true"><circle cx="7" cy="7" r="7" fill="#fff"/><path d="M4.3 3.6l1.4-.3.8 1.8-.9.7c.5 1 1.2 1.7 2.2 2.2l.7-.9 1.8.8-.3 1.4c-3.2 0-6-2.8-6-6z" fill="var(--blue-deep)"/></svg>
        9518 2736
      </p>
      <p class="contact-line">
        <svg class="contact-icon" viewBox="0 0 14 14" aria-hidden="true"><circle cx="7" cy="7" r="7" fill="#fff"/><rect x="3.5" y="4.5" width="7" height="5" fill="none" stroke="var(--blue-deep)" stroke-width="1"/><path d="M3.5 4.5L7 7.3l3.5-2.8" fill="none" stroke="var(--blue-deep)" stroke-width="1"/></svg>
        dunardenwell@mailbox-example.com
      </p>
    </div>
  </section>

  <section class="card card-back" aria-label="Card back">
    <div class="map-area" role="img" aria-label="Faint dotted world map in deep blue behind the company name"></div>
    <div class="brand back-brand">
      <span class="brand-mark"></span>
      <span class="brand-name">Ardenwell</span>
      <span class="brand-tagline">Building and Property Services</span>
    </div>
  </section>

</div>
</body>
</html>
```